Figma App design and working prototype

I need to create a User Interface design and a Working prototype using Figma or similar. I’d also like all the assets and guidelines needed to guide the App developers to create the final product.
So, I'll need Design files and assets but you that I can give to an App development company or a freelance developer to create Android and iOS apps.

This app is an app for adults who wan to meet and have sex no strings attached.

The App name will be Velmora

I have attached an app some pictures and a pdf file explaining details of the apps functions.

This app will be a sexy version of the tavoru app with a personals section used for adult services. I have attached images and a pdf below that will tell you the functions of the app.

I need an app interface design done for an app idea I have. I am nee to this it is my first time trying to launch an app and I do not know what you need in order to get what I need. I need a site map/ design and if possible a working prototype that I can pass on to an app developer that can deliver the final product. This model will be used to raise funds and give investors an idea of what the apps functions will do as detailed in the project brief. Any advise would be greatly appreciated. Please let me know if you have any questions. Looking forward to working with you.

Target Market(s)

Adults men and women looking for some adult entertainment

Industry/Entity Type

Adult entertainment Strip clubs

Colors
E54698
E96AAD
F1A4CE
F9D9EA
FCEFF6
A7469A
B969AE
D3A5CF
EDDBEB
F8F0F9
6B429C
8869AF
B7A5CE
E3DAEB
F3F0F8

Requirements
Must have
• An 18+ confirmation,
Nice to have
• A sexy feel.

```html
<!DOCTYPE html>
<html lang="en">
<head>
<meta charset="utf-8">
<title>Velmora – Navigation Drawer</title>
<link href="https://fonts.googleapis.com/css2?family=Montserrat:wght@500;600;700&display=swap" rel="stylesheet">
<style>
  :root {
    --page-bg: #f3f0f8;
    --brand-pink: #e54698;
    --brand-pink-light: #e96aad;
    --brand-plum: #a7469a;
    --brand-violet: #6b429c;
    --lilac: #b969ae;
    --blush: #f9d9ea;
    --text-muted: #b7a5ce;
    --icon-muted: #b7a5ce;
    --surface: #ffffff;
    --screen-bg: #f8f0f9;
    --card-dark: #2a1f33;
    --photo-warm: #a7469a;
    --photo-soft: #f1a4ce;
    --scrim: rgba(30, 12, 40, 0.42);
  }
  * { box-sizing: border-box; margin: 0; padding: 0; }
  html, body {
    width: 1200px; height: 900px; overflow: hidden;
    background: var(--page-bg);
    font-family: "Montserrat", Arial, sans-serif;
  }
  .canvas {
    width: 1200px; height: 900px;
    display: flex; align-items: center; justify-content: center;
  }
  .app-screen {
    position: relative;
    width: 390px; height: 844px;
    background: var(--screen-bg);
    overflow: hidden;
    box-shadow: 0 18px 50px rgba(107, 66, 156, 0.14);
  }

  /* Home content behind drawer */
  .home-content { position: absolute; inset: 0; }
  .home-search {
    position: absolute; left: 14px; right: 14px; top: 50px; height: 56px;
    background: var(--surface); border-radius: 12px;
  }
  .home-category {
    position: absolute; right: 22px; top: 128px; width: 48px; height: 48px;
    background: var(--surface); border-radius: 12px;
    display: flex; align-items: center; justify-content: center;
  }
  .home-category-label {
    position: absolute; left: 300px; top: 184px;
    font-size: 12px; font-weight: 600; color: var(--brand-pink);
  }
  .home-banner {
    position: absolute; left: 14px; right: 14px; top: 226px; height: 200px;
    background: var(--card-dark); border-radius: 10px;
  }
  .home-listing {
    position: absolute; left: 14px; right: 14px; border-radius: 10px;
  }
  .listing-one { top: 446px; height: 200px; background: linear-gradient(160deg, var(--photo-warm), var(--brand-violet)); }
  .listing-two { top: 664px; height: 180px; background: linear-gradient(160deg, var(--photo-soft), var(--blush)); }
  .badge {
    position: absolute; width: 42px; height: 42px; border-radius: 50%;
    display: flex; align-items: center; justify-content: center;
    font-size: 11px; font-weight: 700; color: #fff;
  }
  .badge-vip { right: 20px; top: 454px; background: var(--lilac); }
  .badge-new { right: 20px; top: 710px; background: var(--brand-pink); }
  .home-tabbar {
    position: absolute; left: 0; right: 0; bottom: 0; height: 70px;
    background: var(--surface);
  }
  .tab-chat {
    position: absolute; right: 22px; bottom: 14px;
    display: flex; flex-direction: column; align-items: center; gap: 4px;
    font-size: 10px; color: var(--text-muted); font-weight: 600;
  }
  .scrim { position: absolute; inset: 0; background: var(--scrim); }

  /* Drawer */
  .drawer {
    position: absolute; top: 0; left: 0; bottom: 0; width: 326px;
    background: var(--surface);
  }
  .drawer-header {
    height: 104px;
    background: linear-gradient(180deg, var(--brand-pink-light), var(--brand-plum));
    display: flex; align-items: flex-end; justify-content: center;
    padding-bottom: 14px;
  }
  .app-name { color: #fff; font-size: 29px; font-weight: 700; letter-spacing: -0.3px; }
  .drawer-welcome {
    text-align: center; margin-top: 12px;
    color: var(--brand-pink); font-size: 32px; font-weight: 600; line-height: 40px;
  }
  .drawer-nav { list-style: none; margin-top: 32px; }
  .nav-item {
    display: flex; align-items: center;
    height: 56px; padding-left: 18px;
    font-size: 16px; font-weight: 700; color: var(--text-muted);
  }
  .nav-item svg { width: 28px; height: 28px; margin-right: 22px; flex-shrink: 0; }
  .nav-item.is-active { color: var(--brand-pink); }
  .age-confirm {
    display: flex; align-items: center; gap: 10px;
    margin: 22px 18px 0; padding: 10px 14px;
    background: var(--blush); border-radius: 10px;
    font-size: 12px; font-weight: 600; color: var(--brand-violet);
  }
  .age-mark {
    width: 30px; height: 30px; border-radius: 50%;
    background: var(--brand-violet); color: #fff;
    display: flex; align-items: center; justify-content: center;
    font-size: 11px; font-weight: 700; flex-shrink: 0;
  }
</style>
</head>
<body>
<main class="canvas">
  <section class="app-screen">
    <div class="home-content" aria-hidden="true">
      <div class="home-search"></div>
      <div class="home-category">
        <svg width="30" height="30" viewBox="0 0 30 30">
          <rect x="2" y="2" width="11" height="11" rx="3" fill="#e54698"/>
          <rect x="17" y="2" width="11" height="11" rx="3" fill="#e54698"/>
          <rect x="2" y="17" width="11" height="11" rx="3" fill="#e54698"/>
          <circle cx="22.5" cy="22.5" r="5" fill="none" stroke="#e54698" stroke-width="2.5"/>
        </svg>
      </div>
      <span class="home-category-label">Categories</span>
      <div class="home-banner"></div>
      <div class="home-listing listing-one" role="img" aria-label="Profile photo of a featured listing"></div>
      <span class="badge badge-vip">VIP</span>
      <div class="home-listing listing-two" role="img" aria-label="Profile photo of a new listing"></div>
      <span class="badge badge-new">New</span>
      <div class="home-tabbar">
        <span class="tab-chat">
          <svg width="24" height="20" viewBox="0 0 24 20"><path d="M3 2h18v12H10l-5 4v-4H3z" fill="none" stroke="#b7a5ce" stroke-width="1.6" stroke-linejoin="round"/></svg>
          Chat
        </span>
      </div>
      <div class="scrim"></div>
    </div>

    <nav class="drawer">
      <header class="drawer-header"><span class="app-name">Velmora</span></header>
      <p class="drawer-welcome">Welcome !</p>
      <ul class="drawer-nav">
        <li class="nav-item is-active">
          <svg viewBox="0 0 28 28"><path d="M3 13 14 4l11 9v12h-7v-8h-8v8H3z" fill="#e54698"/></svg>Home
        </li>
        <li class="nav-item">
          <svg viewBox="0 0 28 28" fill="none" stroke="#b7a5ce" stroke-width="1.6"><circle cx="14" cy="8" r="5"/><path d="M5 26v-3a6 6 0 0 1 6-6h6a6 6 0 0 1 6 6v3z"/></svg>My App
        </li>
        <li class="nav-item">
          <svg viewBox="0 0 28 28" fill="none" stroke="#b7a5ce" stroke-width="1.6"><path d="M3 9h5l2-3h8l2 3h5v14H3z" stroke-linejoin="round"/><circle cx="14" cy="15" r="4.5"/></svg>Post
        </li>
        <li class="nav-item">
          <svg viewBox="0 0 28 28" fill="none" stroke="#b7a5ce" stroke-width="1.6"><path d="M14 24 4.5 14.5a5.5 5.5 0 0 1 9.5-6.5 5.5 5.5 0 0 1 9.5 6.5z" stroke-linejoin="round"/></svg>Favourites
        </li>
        <li class="nav-item">
          <svg viewBox="0 0 28 28" fill="none" stroke="#b7a5ce" stroke-width="1.6"><path d="M3 6h22v13H11l-5 4v-4H3z" stroke-linejoin="round"/><circle cx="9" cy="12.5" r="1" fill="#b7a5ce"/><circle cx="14" cy="12.5" r="1" fill="#b7a5ce"/><circle cx="19" cy="12.5" r="1" fill="#b7a5ce"/></svg>Chat
        </li>
      </ul>
      <div class="age-confirm">
        <span class="age-mark">18+</span>
        <span>Age confirmed · Adults only</span>
      </div>
    </nav>
  </section>
</main>
</body>
</html>
```